Problem Solving Guide- PDF Template

We are looking for an editable PDF template design for our Epoxy Floor Coatings Problem Solving Guide.

Target Market(s)

This guide will be on our website and we will also email it to customers

Industry/Entity Type

Online Shopping

Colors
f78f20
ffffff
5c5c5c
000000

Requirements
Must have
• We are looking for a very modern and clean design. Each page of the guide will address a different issue. There will be 20-25 pages in total for the completed guide, however we just need a template that we can use to create each page so that they look the same. Each page must have our logo, a spot to add a photo of the issue being discussed. Then each page will have the following sections: DESCRIPTION,CAUSE,REPAIR,PREVENTION. At the bottom of each page we would like to direct people to our website for more information. I am attaching the current guide that we have. This shows the basic information that each page will have but as you can see it is old, outdated and anything but modern. As part of the design you can put the different parts of information in circles, squares, use arrows etc. to make it appealing. I am also attaching a copy of our color chart that appears on our website to give you an idea of some of the other graphic designs that we use. Our colors are Orange (please use the same orange as in our logo) grey, black and white. Our website is www.resinmarko.com. There is also a picture of "bubbles in epoxy"-this is an example of a picture we will show to address one issue.

```html
<!DOCTYPE html>
<html lang="en">
<head>
<meta charset="utf-8">
<title>Problem Solving Guide – Color Float</title>
<link href="https://fonts.googleapis.com/css2?family=Source+Sans+3:wght@400;600;700&family=Roboto+Condensed:wght@700&display=swap" rel="stylesheet">
<style>
  :root {
    --orange: #f26522;
    --grey: #6d6e71;
    --grey-dark: #5c5c5c;
    --ink: #3a3a3a;
    --backdrop: #d1d2d4;
    --white: #ffffff;
    --faint: #f1f1f1;
  }
  * { margin: 0; padding: 0; box-sizing: border-box; }
  html, body { width: 1047px; height: 1200px; overflow: hidden; }
  body {
    background: var(--backdrop);
    font-family: "Source Sans 3", "Myriad Pro", Arial, sans-serif;
    color: var(--ink);
    position: relative;
  }
  .page {
    position: absolute;
    left: 111px; top: 121px;
    width: 773px; height: 1000px;
    background: var(--white);
    box-shadow: 6px 6px 8px rgba(0,0,0,0.35);
    overflow: hidden;
  }
  .graphics { position: absolute; left: 0; top: 0; }
  .brand {
    position: absolute;
    right: 32px; top: 118px;
    text-align: right;
  }
  .brand-name {
    display: flex; align-items: center; justify-content: flex-end; gap: 10px;
    font-weight: 700;
    font-size: 50px;
    line-height: 1;
    color: var(--orange);
    letter-spacing: -0.5px;
  }
  .brand-dot {
    width: 22px; height: 22px; border-radius: 50%;
    background: var(--orange);
  }
  .brand-tagline {
    margin-top: 6px;
    font-weight: 700;
    font-size: 16px;
    color: var(--grey);
    letter-spacing: -0.3px;
  }
  .section { position: absolute; left: 23px; width: 714px; }
  .section h2 {
    font-size: 17px;
    font-weight: 700;
    color: var(--orange);
    line-height: 19px;
    margin-bottom: 3px;
  }
  .section p {
    font-size: 16.2px;
    line-height: 20px;
    text-align: justify;
  }
  .section p + p { margin-top: 19px; }
  .description { top: 421px; }
  .description h2 { margin-bottom: 7px; }
  .cause { top: 503px; }
  .repair { top: 649px; }
  .prevention { top: 813px; }

  .footer {
    position: absolute;
    left: 0; bottom: 0;
    width: 773px; height: 50px;
    background: var(--grey);
  }
  .footer-phone {
    position: absolute;
    left: 0; top: 0;
    width: 303px; height: 50px;
    background: var(--orange);
    clip-path: polygon(0 0, 100% 0, 278px 100%, 0 100%);
    display: flex; align-items: center;
    padding-left: 24px;
    gap: 13px;
    color: var(--white);
    font-family: "Roboto Condensed", "Arial Narrow", sans-serif;
    font-weight: 700;
    font-size: 28px;
  }
  .footer-web {
    position: absolute;
    right: 23px; top: 0; height: 50px;
    display: flex; align-items: center; gap: 4px;
    color: var(--white);
    font-size: 11.5px;
  }
  .footer-web .url { font-size: 15.5px; margin-left: 2px; }
  .footer-web .url b { font-weight: 700; }
</style>
</head>
<body>
  <main class="page">
    <svg class="graphics" width="773" height="1000" viewBox="0 0 773 1000">
      <circle class="deco-ring" cx="775" cy="775" r="139" fill="none" stroke="#f1f1f1" stroke-width="38"/>
      <circle cx="185" cy="152" r="223" fill="#f26522"/>
      <circle cx="185" cy="152" r="207" fill="#ffffff"/>
      <circle cx="183" cy="150" r="198" fill="url(#issuePhoto)" role="img" aria-label="Close-up photo of bubbles in an epoxy floor coating"/>
      <circle cx="415" cy="276" r="98" fill="#6d6e71"/>
      <circle cx="415" cy="276" r="90" fill="#ffffff"/>
      <circle cx="415" cy="276" r="86" fill="url(#roomPhoto)" role="img" aria-label="Photo of a modern kitchen with a glossy white epoxy floor"/>
      <defs>
        <radialGradient id="issuePhoto" cx="0.45" cy="0.4" r="0.7">
          <stop offset="0" stop-color="#9a968f"/>
          <stop offset="1" stop-color="#817d77"/>
        </radialGradient>
        <linearGradient id="roomPhoto" x1="0" y1="0" x2="0" y2="1">
          <stop offset="0" stop-color="#3c3f42"/>
          <stop offset="0.45" stop-color="#6b6e70"/>
          <stop offset="0.6" stop-color="#d9dcdc"/>
          <stop offset="1" stop-color="#f2f3f2"/>
        </linearGradient>
      </defs>
    </svg>

    <div class="brand">
      <div class="brand-name"><span class="brand-dot"></span><span>resinmarko</span></div>
      <div class="brand-tagline">Durable resin floors built to last.</div>
    </div>

    <section class="section description">
      <h2>DESCRIPTION</h2>
      <p>Difference in color or shading of topcoat.</p>
    </section>

    <section class="section cause">
      <h2>CAUSE</h2>
      <p>Retouching after 15 minutes: Color float issues arise when a pgmented epoxy has been applied and is re-touch or rooled again after sitting for 15 minutes or longer. Different shadesin the color may result.</p>
      <p>Using different batch numberes: Coloring can vary from batch to batch. Different batches used on the same project can result in color variances.</p>
    </section>

    <section class="section repair">
      <h2>REPAIR</h2>
      <p style="text-align:left">Back rool the entire area always using an 18”, woven, shed-resistant, 3/8” nap roller. Always try to go across the entire area from side-to-side.</p>
      <p>When possible, recoats should alweys be completed with the same coating batsch.</p>
      <p>If batches are different, blend colored (base) side first before adding activator.</p>
    </section>

    <section class="section prevention">
      <h2>PREVENTION</h2>
      <p style="text-align:left">If material needs to be re-touched or rolle for any reason, it needs to be done within 10 minutes of applica-<br>tion.</p>
    </section>

    <footer class="footer">
      <div class="footer-phone">
        <svg width="30" height="30" viewBox="0 0 24 24" aria-hidden="true">
          <path fill="#ffffff" d="M6.6 10.8a15.1 15.1 0 0 0 6.6 6.6l2.2-2.2c.3-.3.7-.4 1-.2 1.1.4 2.3.6 3.6.6.6 0 1 .4 1 1V20c0 .6-.4 1-1 1A17 17 0 0 1 3 4c0-.6.4-1 1-1h3.5c.6 0 1 .4 1 1 0 1.3.2 2.5.6 3.6.1.3 0 .7-.2 1z"/>
          <path fill="none" stroke="#ffffff" stroke-width="1.6" stroke-linecap="round" d="M14 3.5a7 7 0 0 1 6.5 6.5M14 6.5a4 4 0 0 1 3.5 3.5"/>
        </svg>
        <span>1-888-555-0174</span>
      </div>
      <div class="footer-web">
        <span>For additional information and application instructions visit-</span>
        <svg width="13" height="13" viewBox="0 0 14 14" aria-hidden="true">
          <circle cx="7" cy="7" r="6" fill="none" stroke="#ffffff" stroke-width="1.2"/>
          <ellipse cx="7" cy="7" rx="2.6" ry="6" fill="none" stroke="#ffffff" stroke-width="1"/>
          <path d="M1 7h12M2 4h10M2 10h10" stroke="#ffffff" stroke-width="0.9"/>
        </svg>
        <span class="url">www.<b>resinmarko</b>.com</span>
      </div>
    </footer>
  </main>
</body>
</html>
```